Pet and Potrait photography business needs web site design

I need a web design that is for a portrait and pet photography business based in Tasmania, Australia. It is a small, simple concept, photography business that focuses on portraits and pet photography only. I need something that is clean, maybe a white background, fun, and appealing to families. The design must make my images stand out and be the focus. The final design needs to show that it is aimed a families, pet owners, and is all about the clients - albeit the two or four legged kinds.

Business name is: reed and willow photography

I need it to be able to have the following:

- Include space for logo design which is also through SketchHarbor
- Home Page which has a gallery of my images (which you can click an arrow - either forward or back - that showcases my images
- About Page
- Portfolio Page (preferably two a) for portraits, and b) for pet photography
- Pricing page
- secure log in client page
- Contact page

Reason: Waiting for logo design to be completed to fit in with overall website design.

Target Market(s)

Families
Pet owners
Single couples who have fur babies

Industry/Entity Type

Business

Font styles to use
Serif
Decorative
Script

Colors

Designer to choose colors to be used in the design.

Requirements
Must have
• the website must provide the ability for me to upload and change images regularly.
Nice to have
• Logo design is a secondary project that will need to be worked on as well. I will pay an additional amount for those that are prepared to include this in the project.
Should not have
• No graffiti style writing.
It has to be elegant, and stylish and be aimed at females.
Women are going to be the driver for having portraits done of either their babies, children, or fur babies - i.e. pets.

```html
<!DOCTYPE html>
<html lang="en">
<head>
<meta charset="utf-8">
<title>Reed and Willow Photography</title>
<link href="https://fonts.googleapis.com/css2?family=Questrial&family=Merriweather:wght@300&display=swap" rel="stylesheet">
<style>
:root{
  --teal:#a6cdd5;
  --ink:#3f4445;
  --grey:#9a9a9a;
  --text:#7d7d7d;
  --btn:#ececec;
  --line:#dedede;
  --foot:#f1f3f2;
  --dark:#2f3232;
}
*{margin:0;padding:0;box-sizing:border-box}
html,body{width:1013px;height:1200px;overflow:hidden;background:#fff}
body{position:relative;font-family:"Questrial",sans-serif;color:var(--text)}
.abs{position:absolute}
.logo{left:122px;top:24px;color:var(--ink);font-size:30px;line-height:34px;letter-spacing:.5px}
.logo span{display:block;font-size:22px;letter-spacing:2px;color:var(--ink)}
.nav{left:428px;top:69px;display:flex;gap:0;font-size:13px;color:#666}
.nav a{display:block;height:30px;line-height:30px;padding:0 14px;color:#666;text-decoration:none}
.nav a.active{background:var(--teal);color:#fff;border-radius:15px;padding:0 17px}
.hero{left:115px;top:129px;width:764px;height:438px;background:radial-gradient(ellipse at 50% 45%,#d9b9a8 0%,#c7b59a 30%,#b5b490 55%,#9ea78a 80%,#8e9a88 100%)}
.arrow{top:314px;width:69px;height:69px;border:2.5px solid var(--teal);border-radius:50%;display:flex;align-items:center;justify-content:center}
.card{top:463px;width:171px;height:272px;background:#fff;border:2px solid #e4e4e4;border-radius:8px;text-align:center}
.card .icon{width:85px;height:85px;border-radius:50%;background:var(--teal);margin:16px auto 0;display:flex;align-items:center;justify-content:center}
.card h3{font-weight:400;font-size:19px;color:var(--grey);margin-top:11px;letter-spacing:.3px}
.card p{font-family:"Merriweather",serif;font-weight:300;font-size:11.5px;line-height:13.6px;color:var(--text);padding:0 9px;margin-top:6px}
.btn{display:block;background:var(--btn);border-radius:6px;color:#555;font-size:13px;text-align:center;line-height:30px;height:30px}
.card .btn{position:absolute;left:24px;top:218px;width:121px}
.h-small{font-size:18px;color:var(--ink);line-height:20px}
.h-big{font-size:22px;color:var(--grey);line-height:26px}
.para{font-size:11.5px;line-height:13.7px;color:#7a7a7a}
.avatar{left:363px;top:813px;width:134px;height:134px;border-radius:50%;border:4px solid #fff;box-shadow:0 1px 5px rgba(0,0,0,.25);background:radial-gradient(circle at 45% 55%,#4a4a4a 0%,#6b5a50 40%,#a88f80 75%,#d8c6ba 100%)}
.quote{width:36px;height:36px;border-radius:50%;background:var(--teal);display:flex;align-items:center;justify-content:center}
.testi{left:573px;width:292px}
.testi p{font-size:11.5px;line-height:13.7px;color:#7a7a7a}
.testi hr{border:0;border-top:1px dashed #888;margin-top:8px}
.testi .who{font-size:13px;color:var(--teal);margin-top:6px;margin-left:-2px;letter-spacing:.2px}
.footer{left:115px;top:1078px;width:764px;height:122px;background:var(--foot)}
.social{position:absolute;top:33px;width:38px;height:38px;border-radius:50%;background:var(--dark)}
.copy{position:absolute;right:19px;top:41px;font-size:13px;color:#666}
</style>
</head>
<body>

<div class="abs logo">reed and willow<span>photography</span></div>

<nav class="abs nav">
  <a class="active">HOME</a><a>ABOUT</a><a>PORTFOLIO</a><a>PRICING</a><a>LOG IN</a><a>CONTACT</a>
</nav>

<div class="abs hero" role="img" aria-label="Gallery photograph: smiling young girl with windswept hair in a grassy field"></div>

<div class="abs arrow" style="left:21px">
  <svg width="16" height="24" viewBox="0 0 16 24"><path d="M12 3 L4 12 L12 21" fill="none" stroke="#a6cdd5" stroke-width="3"/></svg>
</div>
<div class="abs arrow" style="left:903px">
  <svg width="16" height="24" viewBox="0 0 16 24"><path d="M4 3 L12 12 L4 21" fill="none" stroke="#a6cdd5" stroke-width="3"/></svg>
</div>

<div class="abs card" style="left:126px">
  <div class="icon"><svg width="46" height="52" viewBox="0 0 46 52"><circle cx="23" cy="13" r="12" fill="#fff"/><path d="M2 50 V40 Q2 28 14 28 H32 Q44 28 44 40 V50 Z" fill="#fff"/></svg></div>
  <h3>PORTRAITS</h3>
  <p>Nulla a tristique sem. Morbi ultricies aliquam quam, at molestie nunc bibendu placerat.</p>
  <a class="btn">Visit Gallery</a>
</div>
<div class="abs card" style="left:316px">
  <div class="icon"><svg width="52" height="50" viewBox="0 0 52 50"><ellipse cx="7" cy="20" rx="5.5" ry="7" fill="#fff"/><ellipse cx="18" cy="8" rx="6" ry="7.5" fill="#fff"/><ellipse cx="34" cy="8" rx="6" ry="7.5" fill="#fff"/><ellipse cx="45" cy="20" rx="5.5" ry="7" fill="#fff"/><path d="M26 22 C16 22 10 34 10 40 C10 47 18 47 26 44 C34 47 42 47 42 40 C42 34 36 22 26 22 Z" fill="#fff"/></svg></div>
  <h3>PETS</h3>
  <p>Nulla a tristique sem. Morbi ultricies aliquam quam, at molestie nunc bibendu placerat.</p>
  <a class="btn">Visit Gallery</a>
</div>
<div class="abs card" style="left:506px">
  <div class="icon"><svg width="34" height="48" viewBox="0 0 34 48"><path d="M28 13 Q26 8 17 8 Q7 8 7 15 Q7 21 17 23 Q28 25 28 32 Q28 39 17 39 Q7 39 5 33" fill="none" stroke="#fff" stroke-width="6"/><rect x="14" y="2" width="6" height="44" fill="#fff"/></svg></div>
  <h3>PRICING</h3>
  <p>Nulla a tristique sem. Morbi ultricies aliquam quam, at molestie nunc bibendu placerat.</p>
  <a class="btn">Check Pricing</a>
</div>
<div class="abs card" style="left:696px">
  <div class="icon"><svg width="44" height="44" viewBox="0 0 44 44"><path d="M9 3 L15 3 L19 13 L14 17 Q18 26 27 30 L31 25 L41 29 L41 35 Q38 41 32 41 Q4 33 3 9 Q3 4 9 3 Z" fill="#fff"/></svg></div>
  <h3>CONTACT</h3>
  <p>Nulla a tristique sem. Morbi ultricies aliquam quam, at molestie nunc bibendu placerat.</p>
  <a class="btn">Mail Us</a>
</div>

<div class="abs" style="left:134px;top:762px">
  <div class="h-small">welcome to</div>
  <div class="h-big">Reed and Willow Photography</div>
</div>
<p class="abs para" style="left:134px;top:828px;width:218px">Donec libero diam, lobortis id dolor a, mattis lobortis ante. In velit diam, lobortis in lorem ut, congue dapibus metus. Sed pretium ullamcorper urna, in ullamcorper velit convallis ac. Proin euismod dignissim odio, commodo pharetra libero sollicitudin at. In non est at dui accumsan vestibulum in quis nisi.</p>
<div class="abs avatar" role="img" aria-label="Photograph of the photographer holding a camera"></div>
<p class="abs para" style="left:134px;top:955px;width:360px">Donec libero diam, lobortis id dolor a, mattis lobortis ante. In velit diam, lobortis in lorem ut, congue dapibus metus. Sed pretium ullamcorper urna, in ullamcorper velit convallis ac.</p>
<a class="abs btn" style="left:132px;top:1011px;width:144px">More About Me</a>

<div class="abs" style="left:523px;top:762px">
  <div class="h-small">what others says</div>
  <div class="h-big">About My Photography</div>
</div>

<div class="abs quote" style="left:520px;top:820px"><svg width="20" height="16" viewBox="0 0 20 16"><path d="M1 1 H8 V8 L5 15 H2 L4 8 H1 Z M11 1 H18 V8 L15 15 H12 L14 8 H11 Z" fill="#fff"/></svg></div>
<div class="abs testi" style="top:822px">
  <p>Ut a hendrerit neque. Vestibulum rhoncus quis mauris non porttitor. Nullam vel malesuada sapien. Pellentesque eget volutpat urna, a tempor tortor.</p>
  <hr>
  <div class="who">Nora Hale, CEO Brightfold Studio</div>
</div>

<div class="abs quote" style="left:520px;top:921px"><svg width="20" height="16" viewBox="0 0 20 16"><path d="M1 1 H8 V8 L5 15 H2 L4 8 H1 Z M11 1 H18 V8 L15 15 H12 L14 8 H11 Z" fill="#fff"/></svg></div>
<div class="abs testi" style="top:923px">
  <p>Ut a hendrerit neque. Vestibulum rhoncus quis mauris non porttitor. Nullam vel malesuada sapien. Pellentesque eget volutpat urna, a tempor tortor.</p>
  <hr>
  <div class="who">Nora Hale, CEO Brightfold Studio</div>
</div>
<a class="abs btn" style="left:573px;top:1011px;width:144px">More Testimonial</a>

<footer class="abs footer">
  <span class="social" style="left:18px"></span>
  <span class="social" style="left:68px"></span>
  <span class="social" style="left:118px"></span>
  <span class="social" style="left:168px"></span>
  <span class="social" style="left:218px"></span>
  <div class="copy">© 2013, All Rights Reserved, Reed and Willow Photography</div>
</footer>

</body>
</html>
```